Banner Ad Design Project

I place ads in Clickrow and also get traffic from sites like http://www.wellspringlistings.example.au/ to offer our free meditation CD and report at http://quietmindful.example.au/get-the-free-meditation-cd
We need new designs to improve this campaign.
Target Market(s)
40+ year old women, looking for personal growth or help with stress, depression, anxiety, sleep problems, health issues, memory/concentration issues
Industry/Entity Type
Campaign

```html
<!DOCTYPE html>
<html lang="en">
<head>
<meta charset="utf-8">
<title>Free Meditation CD – Banner Set</title>
<link rel="stylesheet" href="https://fonts.googleapis.com/css2?family=Source+Sans+3:wght@700;900&display=swap">
<style>
  :root{
    --black:#0e0e0e;
    --charcoal:#262626;
    --green:#7cc242;
    --green-dark:#4f8f24;
    --olive:#cbbd4a;
    --red:#ec1c24;
    --yellow:#f7e62a;
    --yellow-deep:#e9cf1c;
    --blue:#1f63b0;
    --blue-deep:#114a8e;
    --white:#ffffff;
    --disc-light:#dfe9f4;
    --disc-mid:#7fa8d2;
    --disc-deep:#3b6ea6;
    --page:#ffffff;
  }
  *{margin:0;padding:0;box-sizing:border-box}
  html,body{width:1200px;height:802px;overflow:hidden;background:var(--page)}
  body{position:relative;font-family:"Source Sans 3","Myriad Pro",Arial,sans-serif}

  .banner{position:absolute;left:32px;width:1140px;height:123px;overflow:hidden}
  .banner--1{top:27px}
  .banner--2{top:195px}
  .banner--3{top:351px}
  .banner--4{top:500px}
  .banner--5{top:654px}

  .banner__bg{position:absolute;inset:0;width:100%;height:100%}
  .banner__texture{position:absolute;inset:0;
    background:repeating-linear-gradient(-60deg,rgba(255,255,255,.07) 0 2px,transparent 2px 7px)}

  .headline{position:absolute;left:24px;top:8px;font-size:40px;font-weight:700;letter-spacing:-.2px;white-space:nowrap;line-height:1}
  .offer{position:absolute;left:55px;font-size:24.5px;font-weight:700;white-space:nowrap;line-height:1}
  .offer--request{top:64px}
  .offer--report{top:96px}

  .cta{position:absolute;left:873px;top:4px;font-size:53px;font-weight:700;line-height:59px;letter-spacing:.5px}
  .banner--3 .cta,.banner--5 .cta{left:858px}
  .banner--3 .cta{left:858px}

  .disc{position:absolute;left:1000px;top:3px;width:117px;height:117px;border-radius:50%;
    background:radial-gradient(circle at 50% 50%,var(--white) 0 10px,var(--disc-light) 11px 22px,var(--disc-mid) 40px,var(--disc-deep) 58px);
    box-shadow:0 0 0 2px rgba(255,255,255,.85)}

  .outline-dark{text-shadow:-1.5px -1.5px 0 #111,1.5px -1.5px 0 #111,-1.5px 1.5px 0 #111,1.5px 1.5px 0 #111,0 2px 0 #111,2px 0 0 #111,-2px 0 0 #111,0 -2px 0 #111}
  .outline-thin{text-shadow:-1px -1px 0 #222,1px -1px 0 #222,-1px 1px 0 #222,1px 1px 0 #222}
  .lifted{text-shadow:1px 2px 2px rgba(0,0,0,.55)}

  .banner--1 .headline,.banner--1 .offer,.banner--1 .cta{color:var(--white)}
  .banner--2 .headline{color:var(--black)}
  .banner--2 .offer,.banner--2 .cta{color:var(--white)}
  .banner--3 .headline{color:var(--black)}
  .banner--3 .offer,.banner--3 .cta{color:var(--white)}
  .banner--4 .headline{color:var(--white)}
  .banner--4 .offer,.banner--4 .cta{color:var(--red)}
  .banner--5 .headline{color:var(--red)}
  .banner--5 .offer,.banner--5 .cta{color:var(--white)}
</style>
</head>
<body>

<!-- Banner 1: black with green divider -->
<section class="banner banner--1">
  <svg class="banner__bg" viewBox="0 0 1140 123" preserveAspectRatio="none" aria-hidden="true">
    <defs>
      <linearGradient id="b1-black" x1="0" y1="0" x2="0" y2="1"><stop offset="0" stop-color="#050505"/><stop offset="1" stop-color="#2e2e2e"/></linearGradient>
      <linearGradient id="b1-green" x1="0" y1="0" x2="0" y2="1"><stop offset="0" stop-color="#8ccd4c"/><stop offset="1" stop-color="#3f7a1c"/></linearGradient>
    </defs>
    <rect width="1140" height="123" fill="url(#b1-black)"/>
    <rect x="821" width="39" height="123" fill="url(#b1-green)"/>
  </svg>
  <div class="banner__texture"></div>
  <h2 class="headline">“How to Meditate Deeper than a Zen Monk!”</h2>
  <p class="offer offer--request">Request today and also receive daily to your inbox</p>
  <p class="offer offer--report">"87 Easy Ways to Instantly Relax Your Mind and Body...FREE"</p>
  <p class="cta">Free<br>CD</p>
  <div class="disc" role="img" aria-label="Meditation CD with a photo of a woman meditating"></div>
</section>

<!-- Banner 2: green with black divider -->
<section class="banner banner--2">
  <svg class="banner__bg" viewBox="0 0 1140 123" preserveAspectRatio="none" aria-hidden="true">
    <defs>
      <linearGradient id="b2-green" x1="0" y1="0" x2="0" y2="1"><stop offset="0" stop-color="#8dcc4e"/><stop offset="1" stop-color="#5a9a2a"/></linearGradient>
      <linearGradient id="b2-black" x1="0" y1="0" x2="0" y2="1"><stop offset="0" stop-color="#3a3a3a"/><stop offset="1" stop-color="#000"/></linearGradient>
    </defs>
    <rect width="1140" height="123" fill="url(#b2-green)"/>
    <rect x="821" width="39" height="123" fill="url(#b2-black)"/>
  </svg>
  <div class="banner__texture"></div>
  <h2 class="headline">“How to Meditate Deeper than a Zen Monk!”</h2>
  <p class="offer offer--request outline-thin">Request today and also receive daily to your inbox</p>
  <p class="offer offer--report outline-thin">"87 Easy Ways to Instantly Relax Your Mind and Body...FREE"</p>
  <p class="cta outline-dark">Free<br>CD</p>
  <div class="disc" role="img" aria-label="Meditation CD with a photo of a woman meditating"></div>
</section>

<!-- Banner 3: olive band over red -->
<section class="banner banner--3">
  <svg class="banner__bg" viewBox="0 0 1140 123" preserveAspectRatio="none" aria-hidden="true">
    <defs>
      <linearGradient id="b3-olive" x1="0" y1="0" x2="1" y2="0"><stop offset="0" stop-color="#c4b84a"/><stop offset="1" stop-color="#f3e536"/></linearGradient>
    </defs>
    <rect width="1140" height="123" fill="var(--red)"/>
    <polygon points="0,0 851,0 829,58 0,58" fill="url(#b3-olive)"/>
  </svg>
  <h2 class="headline">“How to Meditate Deeper than a Zen Monk!”</h2>
  <p class="offer offer--request outline-thin">Request today and also receive daily to your inbox</p>
  <p class="offer offer--report outline-thin">"87 Easy Ways to Instantly Relax Your Mind and Body...FREE"</p>
  <p class="cta outline-dark">Free<br>CD</p>
  <div class="disc" role="img" aria-label="Meditation CD with a photo of a woman meditating"></div>
</section>

<!-- Banner 4: blue band over yellow -->
<section class="banner banner--4">
  <svg class="banner__bg" viewBox="0 0 1140 123" preserveAspectRatio="none" aria-hidden="true">
    <defs>
      <linearGradient id="b4-yellow" x1="0" y1="0" x2="0" y2="1"><stop offset="0" stop-color="var(--yellow)"/><stop offset="1" stop-color="var(--yellow-deep)"/></linearGradient>
      <linearGradient id="b4-blue" x1="0" y1="0" x2="0" y2="1"><stop offset="0" stop-color="#2a74c2"/><stop offset="1" stop-color="var(--blue-deep)"/></linearGradient>
    </defs>
    <rect width="1140" height="123" fill="url(#b4-yellow)"/>
    <polygon points="0,0 851,0 829,58 0,58" fill="url(#b4-blue)"/>
  </svg>
  <div class="banner__texture"></div>
  <h2 class="headline lifted">“How to Meditate Deeper than a Zen Monk!”</h2>
  <p class="offer offer--request lifted">Request today and also receive daily to your inbox</p>
  <p class="offer offer--report lifted">"87 Easy Ways to Instantly Relax Your Mind and Body...FREE"</p>
  <p class="cta lifted">Free<br>CD</p>
  <div class="disc" role="img" aria-label="Meditation CD with a photo of a woman meditating"></div>
</section>

<!-- Banner 5: yellow band over blue -->
<section class="banner banner--5">
  <svg class="banner__bg" viewBox="0 0 1140 123" preserveAspectRatio="none" aria-hidden="true">
    <defs>
      <linearGradient id="b5-blue" x1="0" y1="0" x2="0" y2="1"><stop offset="0" stop-color="#2470be"/><stop offset="1" stop-color="var(--blue-deep)"/></linearGradient>
      <linearGradient id="b5-yellow" x1="0" y1="0" x2="0" y2="1"><stop offset="0" stop-color="var(--yellow)"/><stop offset="1" stop-color="var(--yellow-deep)"/></linearGradient>
    </defs>
    <rect width="1140" height="123" fill="url(#b5-blue)"/>
    <polygon points="0,0 851,0 829,58 0,58" fill="url(#b5-yellow)"/>
  </svg>
  <div class="banner__texture"></div>
  <h2 class="headline outline-thin">“How to Meditate Deeper than a Zen Monk!”</h2>
  <p class="offer offer--request lifted">Request today and also receive daily to your inbox</p>
  <p class="offer offer--report lifted">"87 Easy Ways to Instantly Relax Your Mind and Body...FREE"</p>
  <p class="cta lifted">Free<br>CD</p>
  <div class="disc" role="img" aria-label="Meditation CD with a photo of a woman meditating"></div>
</section>

</body>
</html>
```